Dental Co needs single page print ad

Dental company needs a 1 page ad for trade magazines.
I am uploading an example of what we want (words). We need you to make it look great. It can include people or not.
The uploaded ad isn't there to be copied, just to kind of frame what we are thinking. We are open to any design
One page ad
Size 1)

Trim Size - 8 x 10.5
Bleed Size - 8.25 x 10.75
Live Area - 7 x 10

Size 2)

Trim - 8 x 10.875
Bleed - 8.25 x 11.125
Live Area - 7 x 9.875

BRIX Brand Hex #'s

Orange - ff6319
Teal - 56b1bf
Lt. Teal - aed9da
Blue: #38394B

Target Market(s)

Dentists

Requirements
Must have
• BRIX Logo, pic of the sensor (called VANT)
Use the brand hex colors:
Orange - ff6319
Teal - 56b1bf
Lt. Teal - aed9da
Blue: #38394B

```html
<!DOCTYPE html>
<html lang="en">
<head>
<meta charset="utf-8">
<title>BRIX Imaging – Subscription Sensor Ad</title>
<link href="https://fonts.googleapis.com/css2?family=Outfit:wght@600;700&family=Poppins:wght@400;500;600&family=Kalam:wght@700&display=swap" rel="stylesheet">
<style>
  :root {
    --navy: #101b47;
    --navy-mid: #1f2a52;
    --navy-light: #44506e;
    --orange: #ec5d20;
    --paper: #f6f6f6;
    --white: #ffffff;
  }
  * { box-sizing: border-box; margin: 0; padding: 0; }
  html, body { width: 1070px; height: 1200px; overflow: hidden; background: var(--paper); }
  .ad { position: relative; width: 1070px; height: 1200px; background: var(--paper); overflow: hidden; }
  .backdrop { position: absolute; inset: 0; }
  .headline {
    position: absolute; left: 103px; top: 82px;
    font-family: "Outfit", sans-serif; font-weight: 600;
    font-size: 71px; line-height: 77px; color: var(--white); letter-spacing: 0.2px;
  }
  .aside {
    position: absolute; left: 105px; top: 318px;
    font-family: "Kalam", cursive; font-weight: 700;
    font-size: 28px; color: var(--orange); letter-spacing: 0.5px;
  }
  .price-pill {
    position: absolute; left: 93px; width: 504px; height: 44px;
    background: var(--navy); border-radius: 22px;
    font-family: "Poppins", sans-serif; font-weight: 500;
    font-size: 28px; line-height: 44px; color: var(--white); padding-left: 24px;
  }
  .price-pill.fee { top: 822px; }
  .price-pill.monthly { top: 877px; }
  .benefits { position: absolute; left: 110px; top: 958px; list-style: none; }
  .benefits li {
    display: flex; align-items: center; height: 38px;
    font-family: "Poppins", sans-serif; font-weight: 500; font-size: 18.5px; color: var(--navy);
  }
  .benefits svg { width: 28px; height: 28px; margin-right: 12px; flex: none; }
  .brand { position: absolute; right: 92px; top: 944px; text-align: right; font-family: "Outfit", sans-serif; font-weight: 700; color: var(--navy); }
  .brand .name { font-size: 84px; line-height: 70px; letter-spacing: 1px; }
  .brand .sub { font-size: 34px; line-height: 38px; letter-spacing: 3px; }
  .contact {
    position: absolute; right: 92px; top: 1068px; text-align: right;
    font-family: "Poppins", sans-serif; font-weight: 600; font-size: 30px; line-height: 40px; color: var(--navy);
  }
</style>
</head>
<body>
<main class="ad">
  <svg class="backdrop" width="1070" height="1200" viewBox="0 0 1070 1200">
    <path d="M0,0 H1070 V420 Q900,660 480,692 Q200,705 0,630 Z" fill="var(--navy-light)"/>
    <path d="M0,0 H1070 V290 Q880,590 420,610 Q180,615 0,540 Z" fill="var(--navy-mid)"/>
    <path d="M0,0 H1070 V130 Q900,470 460,500 Q180,510 0,445 Z" fill="var(--navy)"/>
    <circle cx="219" cy="674" r="75" fill="var(--white)"/>
    <circle cx="219" cy="674" r="65" fill="var(--orange)"/>
    <circle cx="681" cy="553" r="242" fill="var(--white)"/>
    <defs>
      <radialGradient id="sensorGlow" cx="50%" cy="42%" r="55%">
        <stop offset="0%" stop-color="#2b3150"/>
        <stop offset="45%" stop-color="#3a2f3a"/>
        <stop offset="100%" stop-color="var(--orange)"/>
      </radialGradient>
    </defs>
    <circle cx="681" cy="553" r="227" fill="url(#sensorGlow)" role="img" aria-label="Product photo of the VANT intra-oral sensor with its cable"/>
  </svg>

  <h1 class="headline">A subscription<br>option for intra-oral<br>sensors is dumb.</h1>
  <p class="aside">(UNTIL YOU DO THE MATH).</p>

  <div class="price-pill fee">$1,999 one-time sign up fee</div>
  <div class="price-pill monthly">$139/mo cancel anytime</div>

  <ul class="benefits">
    <li><svg viewBox="0 0 28 28"><circle cx="14" cy="14" r="13" fill="var(--orange)"/><path d="M8 14.5l4 4 8-9" stroke="#fff" stroke-width="3" fill="none" stroke-linecap="round" stroke-linejoin="round"/></svg>Lifetime $0 deductible warranty</li>
    <li><svg viewBox="0 0 28 28"><circle cx="14" cy="14" r="13" fill="var(--orange)"/><path d="M8 14.5l4 4 8-9" stroke="#fff" stroke-width="3" fill="none" stroke-linecap="round" stroke-linejoin="round"/></svg>Unlimited support &amp; upgrades</li>
    <li><svg viewBox="0 0 28 28"><circle cx="14" cy="14" r="13" fill="var(--orange)"/><path d="M8 14.5l4 4 8-9" stroke="#fff" stroke-width="3" fill="none" stroke-linecap="round" stroke-linejoin="round"/></svg>Direct integration w/all major software</li>
    <li><svg viewBox="0 0 28 28"><circle cx="14" cy="14" r="13" fill="var(--orange)"/><path d="M8 14.5l4 4 8-9" stroke="#fff" stroke-width="3" fill="none" stroke-linecap="round" stroke-linejoin="round"/></svg>Affordable enough for every op</li>
    <li><svg viewBox="0 0 28 28"><circle cx="14" cy="14" r="13" fill="var(--orange)"/><path d="M8 14.5l4 4 8-9" stroke="#fff" stroke-width="3" fill="none" stroke-linecap="round" stroke-linejoin="round"/></svg>Preserve your capital</li>
  </ul>

  <div class="brand">
    <div class="name">BRIX</div>
    <div class="sub">IMAGING</div>
  </div>
  <address class="contact" style="font-style:normal">
    (555) 210-BRIX<br>www.briximaging.com
  </address>
</main>
</body>
</html>
```